Not your average candle company needs label design

MOSS + RUIN A Brand Deck for Disruptive Candles
WHO WE ARE
Moss + Ruin is a disruptive candle brand built on contrast. We create clean-burning, scent-forward rituals for people who are both grounded and undone.
We’re not here for the beige wellness aesthetic. We’re here for the moments that are messy, bold, emotional, and beautifully real.
Rooted in botanical craftsmanship. Branded in poetic defiance.
WHAT WE WANT PEOPLE TO THINK
When someone encounters Moss + Ruin, we want them to feel like they’ve stumbled into something intimate, moody, and unforgettable.
We want them to think:
• “This brand gets me.”
• “This feels like design, emotion, and scent in one.”
• “It’s art I can burn.”
• “I’ve never seen a candle brand like this before.”
Our name alone sparks curiosity. Our story keeps them. Our product delivers.

Target Market(s)

Women and men ages 25–45 who appreciate thoughtful design and emotional storytelling People who love brands like Farvale, Kid Whiffs, Pelican Grange, Mivune, and Du Vanto Design-minded buyers who shop indie, high-end, or artisanal and care about self-expression through scent Emotionally intelligent rebels. Introspective, edgy, but craving grounding rituals.

Industry/Entity Type

Candle Industry

Font styles to use
Other font styles liked:
• Moss should be more refined in a serif font and I like mistrully font for ruin.

Requirements
Must have
• Space for scent name and optionally, a small poetic tagline (like soft chaos. slow burn.) Layout that’s elegant but with tension — surprise us with something that doesn't play it safe Optional: room for batch no., burn time, scent notes on side or bottom. MOSS + RUIN soft chaos. slow burn. Scent name example: Lanternfall A silent vow to stay grounded. Earthy and grounding — like old books, soft shadows, and the quiet certainty of knowing who you are. [optional: 7 oz / 198g | coconut soy wax | 45+ hr burn time]
Nice to have
• raw edge opening with gold font. Open to colored labels. We’re creating an unforgettable candle brand called Moss + Ruin — a contrast-rich, emotionally resonant collection of candles that blend botanical beauty with bold edge. The name is intentional: Moss reflects grounding, ritual, and plant-based purity; Ruin speaks to vulnerability, chaos, and strength through contrast. Our brand is not dark or gothic — it’s confident, elevated, and style-forward, with packaging that feels like a cross between modern apothecary and high fashion. Think Mivune meets Dale Pruitt. Gloss vessels, textured labels, contrasting fonts, and emotional scent storytelling.
Should not have
• goth vibe, typical candle label template layout.

```html
<!DOCTYPE html>
<html lang="en">
<head>
<meta charset="utf-8">
<title>Moss + Ruin — Packaging Concepts</title>
<link rel="stylesheet" href="https://fonts.googleapis.com/css2?family=Archivo+Black&family=Barlow:wght@400;500&family=Playfair+Display:wght@600&display=swap">
<style>
  :root {
    --forest: #032e25;
    --forest-deep: #022820;
    --leaf: #1fa34a;
    --moss: #4f7c35;
    --ink: #16161a;
    --paper: #ffffff;
    --caption: #a3a3a3;
    --cream: #f3d6b8;
    --gold: #c9a77a;
    --bronze: #a87238;
    --table: #66553f;
  }
  * { margin: 0; padding: 0; box-sizing: border-box; }
  html, body { width: 1200px; height: 1195px; overflow: hidden; background: var(--paper); }
  .board { position: relative; width: 1200px; height: 1195px; font-family: "Barlow", sans-serif; }

  .masthead {
    position: absolute; left: 3px; top: 2px; width: 1197px; height: 173px;
    background: var(--forest);
  }
  .studio-mark {
    position: absolute; left: 62px; top: 66px;
    display: flex; align-items: center; gap: 10px;
    color: var(--leaf); font-weight: 500; font-size: 20px; letter-spacing: 0.08em;
  }
  .studio-mark__square { width: 34px; height: 34px; border: 2px solid var(--leaf); }
  .masthead__titles {
    position: absolute; left: 708px; top: 64px;
    display: grid; grid-template-columns: 140px auto; row-gap: 4px;
    font-size: 25px; line-height: 29px; letter-spacing: 0.02em;
  }
  .masthead__key { color: var(--paper); }
  .masthead__value { color: var(--leaf); }

  .section-tag {
    position: absolute; color: var(--caption);
    font-size: 14px; line-height: 18px; letter-spacing: 0.06em;
  }
  .section-tag--logo { left: 65px; top: 282px; }
  .section-tag--label { left: 65px; top: 569px; }
  .section-tag--mockup { left: 600px; top: 569px; color: #c9cfcc; z-index: 2; }

  .wordmark {
    position: absolute; left: 380px; top: 300px; width: 440px; text-align: center;
    font-family: "Playfair Display", serif; font-weight: 600;
    font-size: 78px; line-height: 1; color: var(--ink);
  }

  .label {
    position: absolute; left: 192px; top: 560px; width: 227px; height: 586px;
    background: var(--forest);
  }
  .label__brand {
    position: absolute; left: 0; top: 100px; width: 100%; text-align: center;
    font-family: "Playfair Display", serif; font-weight: 600;
    font-size: 36px; color: var(--moss);
  }
  .label__band {
    position: absolute; left: 0; top: 258px; width: 100%; height: 24px;
    background: linear-gradient(90deg, var(--cream) 0%, #ecd4b0 45%, var(--gold) 75%, var(--bronze) 100%);
  }
  .label__wax {
    position: absolute; left: 0; top: 317px; width: 100%; text-align: center;
    font-family: "Archivo Black", sans-serif; font-size: 13px; line-height: 18px;
    color: var(--paper);
  }
  .label__scent {
    position: absolute; left: 0; top: 386px; width: 100%; text-align: center;
    font-family: "Playfair Display", serif; font-weight: 600;
    font-size: 36px; line-height: 40px;
  }
  .label__scent span { display: block; }
  .label__scent .first { color: var(--cream); }
  .label__scent .second { color: var(--bronze); }
  .label__specs {
    position: absolute; left: 0; top: 505px; width: 100%; text-align: center;
    font-family: "Archivo Black", sans-serif; font-size: 8px; line-height: 12px;
    color: var(--paper);
  }
  .label__specs .divider { color: var(--leaf); }

  .mockup-panel {
    position: absolute; left: 555px; top: 509px; width: 645px; height: 686px;
    background: var(--forest); overflow: hidden;
  }
  .mockup-photo {
    position: absolute; left: 0; top: 100px; width: 645px; height: 586px;
    background: linear-gradient(170deg, var(--forest) 0%, var(--forest) 40%, #3d4a35 60%, var(--table) 78%, #5c4b37 100%);
  }
</style>
</head>
<body>
<main class="board">
  <header class="masthead">
    <div class="studio-mark"><span class="studio-mark__square"></span>KELP STUDIO</div>
    <div class="masthead__titles">
      <span class="masthead__key">PARTNER</span><span class="masthead__value">MOSS + RUIN</span>
      <span class="masthead__key">DOCUMENT</span><span class="masthead__value">PACKAGING CONCEPTS</span>
    </div>
  </header>

  <div class="section-tag section-tag--logo">1.0<br>LOGO</div>
  <div class="wordmark">Moss + Ruin</div>

  <div class="section-tag section-tag--label">2.0<br>LABEL</div>
  <section class="label">
    <div class="label__brand">Moss + Ruin</div>
    <div class="label__band"></div>
    <div class="label__wax">COCONUT<br>SOY WAX</div>
    <h2 class="label__scent"><span class="first">Lantern</span><span class="second">fall</span></h2>
    <div class="label__specs">7 oz <span class="divider">|</span> 198g<br>45+ HR BURN TIME</div>
  </section>

  <section class="mockup-panel">
    <div class="mockup-photo" role="img" aria-label="Photo of the labelled candle box beside a lit-ready glass candle on a brown tabletop"></div>
  </section>
  <div class="section-tag section-tag--mockup">3.0<br>MOCKUP</div>
</main>
</body>
</html>
```